Stylish new business card needed!

Hello everyone! I am in need of a new business card design for an alarm company here in Hurricane WV. I have all fonts, color codes and logos provided for you use! We are a young company and like the style of a clean sleek looking business card. Would like it double sided, one side holding the logo and the other with your design!
Target Market(s)
The people that are looking for the newest tech for home automation and security
Industry/Entity Type
Alarm services; Home automation
Contact Information for Business Card
Name of person; position (Sales; Installer); Phone Number (555.418.7290); Employee cell Number; Website (www.GuardedByVemlo.example); Employee Email; Double sided
Look and feel
Each slider illustrates characteristics of the customer's brand and the style your logo design should communicate.

```html
<!DOCTYPE html>
<html lang="en">
<head>
<meta charset="utf-8">
<title>Guarded By Vemlo – Business Card</title>
<link rel="stylesheet" href="https://fonts.googleapis.com/css2?family=Lato:ital,wght@0,400;0,900;1,400&display=swap">
<style>
  :root {
    --brand-orange: #fb8c4b;
    --ink-grey: #555555;
    --paper: #ffffff;
    --backdrop: #1c1c1c;
  }
  * { box-sizing: border-box; margin: 0; padding: 0; }
  html, body {
    width: 1200px; height: 1156px; overflow: hidden;
    background: var(--backdrop);
    font-family: "Lato", Arial, sans-serif;
  }
  .canvas {
    width: 1200px; height: 1156px;
    display: flex; flex-direction: column; align-items: center; justify-content: center;
    gap: 44px;
  }
  .card {
    position: relative;
    width: 900px; height: 514px;
    overflow: hidden;
  }
  /* Front side */
  .card--front { background: var(--paper); }
  .wordmark {
    position: absolute; left: 64px; top: 56px;
    color: var(--brand-orange);
  }
  .wordmark__name {
    font-weight: 900; font-size: 44px; letter-spacing: 2px; line-height: 1;
    text-transform: uppercase;
  }
  .wordmark__tagline {
    margin-top: 12px;
    font-weight: 900; font-size: 13px; letter-spacing: 1.6px;
    text-transform: uppercase;
  }
  .divider {
    position: absolute; left: 64px; right: 64px; top: 316px;
    height: 2px; background: var(--brand-orange);
  }
  .holder {
    position: absolute; right: 64px; top: 232px; text-align: right;
  }
  .holder__name {
    font-weight: 900; font-size: 36px; letter-spacing: 1px; line-height: 1;
    color: var(--brand-orange); text-transform: uppercase;
  }
  .holder__role {
    margin-top: 6px; font-size: 20px; color: var(--ink-grey);
  }
  .contacts {
    position: absolute; left: 64px; top: 344px;
    list-style: none;
  }
  .contacts__item {
    display: flex; align-items: center; gap: 12px;
    font-style: italic; font-size: 22px; line-height: 34px; color: var(--ink-grey);
  }
  .contacts__icon { width: 18px; height: 18px; flex: none; }
  /* Back side */
  .card--back {
    background: var(--brand-orange);
    display: flex; align-items: center; justify-content: center;
  }
  .card--back .wordmark {
    position: static; color: var(--paper); text-align: center;
  }
  .card--back .wordmark__name { font-size: 64px; letter-spacing: 3px; }
  .card--back .wordmark__tagline { font-size: 18px; margin-top: 16px; letter-spacing: 2.4px; }
</style>
</head>
<body>
<main class="canvas">
  <section class="card card--front">
    <div class="wordmark">
      <div class="wordmark__name">Guarded By Vemlo</div>
      <div class="wordmark__tagline">Automation and Security Services</div>
    </div>

    <div class="holder">
      <div class="holder__name">Dale Harrow</div>
      <div class="holder__role">Manager</div>
    </div>

    <div class="divider"></div>

    <ul class="contacts">
      <li class="contacts__item">
        <svg class="contacts__icon" viewBox="0 0 18 18"><rect x="4" y="1" width="10" height="16" rx="2" fill="none" stroke="var(--brand-orange)" stroke-width="2"/><circle cx="9" cy="14" r="1" fill="var(--brand-orange)"/></svg>
        000-000-0000
      </li>
      <li class="contacts__item">
        <svg class="contacts__icon" viewBox="0 0 18 18"><path d="M4 2 L7 2 L8 6 L6 7.5 Q8 11 10.5 12 L12 10 L16 11 L16 14 Q16 16 14 16 Q3 15 2 4 Q2 2 4 2 Z" fill="var(--brand-orange)"/></svg>
        555.418.7290
      </li>
      <li class="contacts__item">
        <svg class="contacts__icon" viewBox="0 0 18 18"><rect x="1" y="4" width="16" height="11" fill="var(--brand-orange)"/><path d="M1 4 L9 10 L17 4" fill="none" stroke="var(--paper)" stroke-width="1.5"/></svg>
        mail@GuardedByVemlo.example
      </li>
      <li class="contacts__item">
        <svg class="contacts__icon" viewBox="0 0 18 18"><circle cx="9" cy="9" r="8" fill="var(--brand-orange)"/><path d="M1 9 H17 M9 1 Q4 9 9 17 M9 1 Q14 9 9 17" fill="none" stroke="var(--paper)" stroke-width="1.2"/></svg>
        www.GuardedByVemlo.example
      </li>
    </ul>
  </section>

  <section class="card card--back">
    <div class="wordmark">
      <div class="wordmark__name">Guarded By Vemlo</div>
      <div class="wordmark__tagline">Automation and Security Services</div>
    </div>
  </section>
</main>
</body>
</html>
```